Logo/Business Card design for a Chef using Tattoo Inspiration- Design must meet business card requirements on Pellu's website - link below

Business Card/Logo Design for my little brother- I would like to design and order my brother business cards for his business. He has a passion for cooking and was recently promoted to head chef. I have a picture of his tattoo that I would like re-imagined so it can be incorporate in the design of the business card or used to create a logo.
Must haves
1. Tattoo incorporated into the design
2. card Details below
must be able to use design to create the business card on Pellu.
Card details:
Business Name: Spoon And Ember
Name: Dennis Holloway
Title: Private Chef
Phone: 408-555-0172
Instragram: spoon_and_ember

optional use: via text or pictures incorporated in card design.
specialized in Korean, Italian, Peruvian, American, Chinese.
Private Chef
Dinner Parties
Special Occasions

type of card Square with round edges: the picture of his tattoo incorporated within the design.
Square Business Card templates to download https://help.pellu-example.com/hc/en-us/articles/500000001-Square-Business-Card-templates-to-download
Create business card here using their requirements.
https://www.pellu-example.com/us/design-templates/business-cards/?finishingOption=square_corners&laminate=mattelam&origPaperType=classic&paperType=classic&productType=businesscard_us
Card details

```html
<!DOCTYPE html>
<html lang="en">
<head>
<meta charset="utf-8">
<title>Spoon And Ember — Business Cards</title>
<link rel="stylesheet" href="https://fonts.googleapis.com/css2?family=Poppins:wght@300;400;800&display=swap">
<style>
  :root {
    --stage-top: #3a3a3a;
    --stage-bottom: #1c1c1c;
    --card: #111111;
    --card-edge: #1d1d1d;
    --ember: #e2202a;
    --ink: #e8e8e8;
    --ink-soft: #bdbdbd;
  }
  * { box-sizing: border-box; margin: 0; padding: 0; }
  html, body {
    width: 1200px;
    height: 900px;
    overflow: hidden;
  }
  body {
    background: radial-gradient(ellipse at 50% 35%, var(--stage-top), var(--stage-bottom) 75%);
    font-family: "Poppins", sans-serif;
    position: relative;
  }
  .card {
    position: absolute;
    width: 540px;
    height: 309px;
    background: var(--card);
    border: 1px solid var(--card-edge);
    box-shadow: 0 18px 40px rgba(0,0,0,0.55);
    overflow: hidden;
  }
  .card--back { left: 600px; top: 110px; }
  .card--front { left: 70px; top: 470px; }

  .wordmark {
    position: absolute;
    display: flex;
    align-items: center;
    gap: 10px;
    font-family: "Poppins", sans-serif;
    font-weight: 800;
    font-size: 30px;
    letter-spacing: 0.5px;
    text-transform: uppercase;
    color: var(--ember);
    white-space: nowrap;
  }
  .wordmark__dot {
    width: 14px;
    height: 14px;
    border-radius: 50%;
    background: var(--ember);
  }
  .card--back .wordmark { left: 0; right: 0; top: 112px; justify-content: center; }
  .card--front .wordmark { left: 230px; top: 88px; font-size: 26px; }

  .specialties {
    position: absolute;
    font-weight: 300;
    color: var(--ink-soft);
    font-size: 15px;
    line-height: 1.45;
  }
  .card--back .specialties { left: 0; right: 0; top: 190px; text-align: center; }
  .card--front .specialties { left: 262px; top: 206px; font-size: 16px; }

  .contact {
    position: absolute;
    left: 26px;
    top: 42px;
    width: 200px;
  }
  .contact__name {
    display: flex;
    align-items: center;
    gap: 8px;
    color: var(--ember);
    font-size: 18px;
    font-weight: 400;
  }
  .contact__title {
    color: var(--ink-soft);
    font-weight: 300;
    font-size: 14px;
    margin: 6px 0 0 26px;
  }
  .contact__rule {
    height: 2px;
    background: var(--ember);
    margin: 10px 0 12px 0;
    width: 190px;
  }
  .contact__row {
    display: flex;
    align-items: center;
    gap: 10px;
    color: var(--ink-soft);
    font-weight: 300;
    font-size: 14px;
    margin-bottom: 8px;
  }
  .contact svg { flex: none; }
</style>
</head>
<body>

  <section class="card card--back" aria-label="Business card back">
    <div class="wordmark"><span class="wordmark__dot"></span>Spoon And Ember</div>
    <p class="specialties">specialized in Korean, Italian, Peruvian, American, Chinese.</p>
  </section>

  <section class="card card--front" aria-label="Business card front">
    <div class="contact">
      <div class="contact__name">
        <svg width="18" height="18" viewBox="0 0 18 18" aria-hidden="true">
          <circle cx="9" cy="5.5" r="3.8" fill="none" stroke="#e8e8e8" stroke-width="1.5"/>
          <path d="M2 17c0-4 3-6.5 7-6.5s7 2.5 7 6.5" fill="none" stroke="#e8e8e8" stroke-width="1.5"/>
        </svg>
        Dennis Holloway
      </div>
      <p class="contact__title">Private Chef</p>
      <div class="contact__rule"></div>
      <div class="contact__row">
        <svg width="14" height="14" viewBox="0 0 24 24" aria-hidden="true">
          <path d="M6.6 10.8a15.1 15.1 0 0 0 6.6 6.6l2.2-2.2a1 1 0 0 1 1-.25 11.4 11.4 0 0 0 3.6.57 1 1 0 0 1 1 1V20a1 1 0 0 1-1 1A17 17 0 0 1 3 4a1 1 0 0 1 1-1h3.5a1 1 0 0 1 1 1c0 1.25.2 2.45.57 3.6a1 1 0 0 1-.25 1z" fill="#e2202a"/>
        </svg>
        408-555-0172
      </div>
      <div class="contact__row">
        <svg width="14" height="14" viewBox="0 0 14 14" aria-hidden="true">
          <rect x="1" y="1" width="12" height="12" fill="#e2202a"/>
        </svg>
        spoon_and_ember
      </div>
    </div>

    <div class="wordmark"><span class="wordmark__dot"></span>Spoon And Ember</div>

    <p class="specialties">specialized in Korean, Italian,<br>Peruvian, American, Chinese.</p>
  </section>

</body>
</html>
```